PowerPoint Design Project for Veltro Bonding AB - a innovative adhesives company

We are looking to lift our current sales PPT template to convey a professional maturer image. Veltro Bonding AB (www.veltrobonding.example) develop a unique switchable adhesive that can be used in many different industries. Our strength in our technology is that the adhesive is stronger yet easier to remove in the same product.
We want to maintain our logo including its font (see attached).
We want to convey innovation, trustworthiness, Nordic (Sweden based) and high end (high tech) products.
Target Market(s)
Product managers, technical product owners, upper management, higher education levels.
Industry/Entity Type
It Company
Requirements
Must have
- 1) Existing logo
2) Index for presentation
3) Page numbers - or cool progress indicator indicating how much is left of the presentation
4) End slide - including contact details
5) Indicator of confidentiality
6) Headers, sub-headers, bullets synced (style)
Should not have
- Sounds and animations

```html
<!DOCTYPE html>
<html lang="en">
<head>
<meta charset="utf-8">
<title>Veltro Bonding – Presentation Template</title>
<link href="https://fonts.googleapis.com/css2?family=Arimo:wght@400;700&display=swap" rel="stylesheet">
<style>
:root{
  --canvas:#e4e4e4;
  --white:#ffffff;
  --blue:#12b3e3;
  --blue-deep:#0ea2d3;
  --blue-light:#35c6ee;
  --ink:#222222;
  --grey-text:#555555;
  --grey-soft:#9a9a9a;
  --bar-grey:#8c8c8c;
  --line-grey:#b8b8b8;
}
*{margin:0;padding:0;box-sizing:border-box}
html,body{width:1200px;height:900px;overflow:hidden;background:var(--canvas);font-family:"Arimo",Arial,sans-serif;color:var(--ink)}
.sheet{position:relative;width:1200px;height:900px}
.slide{position:absolute;width:372px;height:279px;background:var(--white);box-shadow:2px 3px 6px rgba(0,0,0,.35);overflow:hidden}
.c1{left:21px}.c2{left:414px}.c3{left:807px}
.r1{top:15px}.r2{top:310px}.r3{top:605px}

.footer{position:absolute;bottom:4px;left:0;width:100%;text-align:center;font-size:4px;color:var(--grey-soft)}
.page-no{position:absolute;bottom:4px;right:20px;font-size:6px;color:var(--blue)}

.wordmark{font-weight:700;letter-spacing:.5px;white-space:nowrap;display:flex;align-items:center;gap:4px}
.wordmark .dot{display:inline-block;border-radius:50%;background:var(--blue)}
.wordmark.on-blue{color:var(--white)}
.wordmark.on-blue .dot{background:var(--white)}

.title-band{position:absolute;left:5px;right:5px;top:202px;height:50px;background:linear-gradient(var(--blue-light),var(--blue-deep));border-radius:2px;color:var(--white);text-align:center;padding-top:11px}
.title-band h1{font-size:12.5px;font-weight:400}
.title-band p{font-size:7.5px;margin-top:8px}

.logo-disc{position:absolute;left:120px;top:47px;width:133px;height:133px;border-radius:50%;background:radial-gradient(circle at 50% 35%,#ffffff 0%,#f2f2f2 55%,#d6d6d6 100%);box-shadow:0 3px 6px rgba(0,0,0,.2);display:flex;align-items:center;justify-content:center}

.hero{position:absolute;left:8px;right:8px;top:8px;height:192px;background:linear-gradient(var(--blue-light),var(--blue-deep));display:flex;align-items:center;justify-content:center;padding-bottom:10px}
.hero-caption{position:absolute;left:0;width:100%;text-align:center;color:var(--grey-text)}
.foot-bar{position:absolute;left:8px;right:8px;top:248px;height:22px;background:var(--blue)}

.agenda{background:linear-gradient(var(--blue-light),var(--blue-deep))}
.agenda h2{position:absolute;left:23px;top:56px;color:var(--white);font-size:14px;font-weight:700}
.agenda ul{position:absolute;left:19px;top:80px;width:333px;list-style:none;color:var(--white);font-size:7.5px}
.agenda li{padding:1.5px 5px;line-height:9px}
.agenda li.current{border:1px solid rgba(255,255,255,.7);border-radius:2px}

.slide-head{position:absolute;left:23px;top:19px;width:335px;font-size:13px;font-weight:400;color:var(--blue);padding-bottom:3px;border-bottom:1px solid #bfe6f4}
.bullets{list-style:none;font-size:7px;line-height:9.5px;color:var(--grey-text)}
.bullets li{position:relative;padding-left:8px;margin-bottom:8px}
.bullets li::before{content:"•";position:absolute;left:0;color:var(--blue)}
.corner-mark{position:absolute;left:19px;bottom:6px}

.end-logo{position:absolute;left:80px;top:77px;width:212px;height:58px;background:#f4f4f4;box-shadow:0 4px 6px rgba(0,0,0,.25);display:flex;flex-direction:column;align-items:center;justify-content:center;gap:5px}
.end-logo .url{font-size:4.5px;color:var(--grey-soft);letter-spacing:.6px}
.thanks{position:absolute;left:0;width:100%;top:182px;text-align:center;color:var(--blue-deep);font-size:9.5px;font-weight:700}
.contact{position:absolute;left:0;width:100%;top:221px;text-align:center;font-size:5px;color:var(--grey-text);line-height:13px}
svg text{font-family:"Arimo",Arial,sans-serif}
</style>
</head>
<body>
<div class="sheet">

  <!-- Title option A -->
  <section class="slide c1 r1">
    <div class="logo-disc">
      <div class="wordmark" style="font-size:13px;color:var(--ink)">VELTRO BONDING <span class="dot" style="width:8px;height:8px"></span></div>
    </div>
    <div class="title-band">
      <h1>Insert The Title of Your Presentation Here</h1>
      <p>Subtitle of the Presentation or main author’s name here</p>
    </div>
    <div class="footer">© 2013 Veltro Bonding. All Rights Reserved.</div>
  </section>

  <!-- Title option B -->
  <section class="slide c2 r1">
    <div class="wordmark" style="position:absolute;left:0;width:100%;top:100px;justify-content:center;font-size:26px;color:var(--ink)">VELTRO BONDING <span class="dot" style="width:16px;height:16px"></span></div>
    <div class="title-band">
      <h1>Insert The Title of Your Presentation Here</h1>
      <p>Subtitle of the Presentation or main author’s name here</p>
    </div>
    <div class="footer">© 2013 Veltro Bonding. All Rights Reserved.</div>
  </section>

  <!-- Title option C -->
  <section class="slide c3 r1">
    <div class="hero"><div class="wordmark on-blue" style="font-size:28px">VELTRO BONDING <span class="dot" style="width:18px;height:18px"></span></div></div>
    <div class="hero-caption" style="top:213px;font-size:12px">Insert The Title of Your Presentation Here</div>
    <div class="hero-caption" style="top:232px;font-size:7px">Subtitle of the Presentation or main author’s name here</div>
    <div class="foot-bar"></div>
    <div class="footer">© 2013 Veltro Bonding. All Rights Reserved.</div>
  </section>

  <!-- Agenda -->
  <section class="slide agenda c1 r2">
    <h2>Agenda</h2>
    <ul>
      <li class="current">• Chapter 1</li>
      <li>• Chapter 2</li>
      <li>• Chapter 3</li>
    </ul>
    <div class="footer" style="color:rgba(255,255,255,.7)">© 2013 Veltro Bonding. All Rights Reserved.</div>
  </section>

  <!-- Text slide -->
  <section class="slide c2 r2">
    <h2 class="slide-head">Text slide</h2>
    <ul class="bullets" style="position:absolute;left:23px;top:70px;width:330px">
      <li>Lorem ipsum dolor sit amet, consectetur adipiscing elit. Duis blandit lorem eu libero congue aliquam vel sit amet augue. Mauris augue ipsum, dignissim vitae adipiscing eu, euismod nec sem.</li>
      <li>Lorem ipsum dolor sit amet, consectetur adipiscing elit. Duis blandit lorem eu libero congue aliquam vel sit amet augue. Mauris augue ipsum, dignissim vitae adipiscing eu, euismod nec sem.</li>
      <li>Lorem ipsum dolor sit amet, consectetur adipiscing elit. Duis blandit lorem eu libero congue aliquam vel sit amet augue. Mauris augue ipsum, dignissim vitae adipiscing eu, euismod nec sem.</li>
      <li>Lorem ipsum dolor sit amet, consectetur adipiscing elit. Duis blandit lorem eu libero congue aliquam vel sit amet augue. Mauris augue ipsum, dignissim vitae adipiscing eu, euismod nec sem.</li>
    </ul>
    <div class="wordmark corner-mark" style="font-size:7px;color:var(--ink)">VELTRO BONDING <span class="dot" style="width:5px;height:5px"></span></div>
    <div class="footer">© 2013 Veltro Bonding. All Rights Reserved.</div>
    <div class="page-no">7</div>
  </section>

  <!-- Bar chart slide -->
  <section class="slide c3 r2">
    <h2 class="slide-head">Graph Slide – Example 1</h2>
    <svg style="position:absolute;left:0;top:0" width="190" height="279" viewBox="0 0 190 279">
      <defs>
        <linearGradient id="barBlue" x1="0" y1="0" x2="0" y2="1"><stop offset="0" stop-color="#45cdf1"/><stop offset="1" stop-color="#0ea2d3"/></linearGradient>
        <linearGradient id="barGrey" x1="0" y1="0" x2="0" y2="1"><stop offset="0" stop-color="#aaaaaa"/><stop offset="1" stop-color="#7a7a7a"/></linearGradient>
      </defs>
      <text x="105" y="83" font-size="6.5" font-weight="700" fill="#444" text-anchor="middle">Graph Title</text>
      <line x1="62" y1="90" x2="62" y2="232" stroke="#ccc" stroke-width=".6"/>
      <g font-size="5.5" fill="#444">
        <text x="56" y="114" text-anchor="end">1st Qtr</text>
        <text x="56" y="150" text-anchor="end">2nd Qtr</text>
        <text x="56" y="186" text-anchor="end">3rd Qtr</text>
        <text x="56" y="222" text-anchor="end">4th Qtr</text>
      </g>
      <rect x="62" y="102" width="93" height="17" fill="url(#barBlue)"/>
      <rect x="62" y="138" width="36" height="17" fill="url(#barGrey)"/>
      <rect x="62" y="174" width="16" height="17" fill="url(#barGrey)"/>
      <rect x="62" y="210" width="14" height="17" fill="url(#barGrey)"/>
      <g font-size="5.5" fill="#444">
        <text x="158" y="113">8,2</text>
        <text x="101" y="149">3,2</text>
        <text x="81" y="185">1,4</text>
        <text x="79" y="221">1,2</text>
      </g>
    </svg>
    <ul class="bullets" style="position:absolute;left:184px;top:100px;width:165px;font-size:6.3px;line-height:8.5px">
      <li>Lorem ipsum dolor sit amet, consectetur adipiscing elit. Duis blandit lorem eu libero congue aliquam vel sit amet augue. Mauris augue ipsum, dignissim vitae adipiscing eu, euismod nec sem.</li>
      <li>Lorem ipsum dolor sit amet, consectetur adipiscing elit. Duis blandit lorem eu libero congue aliquam vel sit amet augue. Mauris augue ipsum, dignissim vitae adipiscing eu, euismod nec sem.</li>
    </ul>
    <div class="wordmark corner-mark" style="font-size:7px;color:var(--ink)">VELTRO BONDING <span class="dot" style="width:5px;height:5px"></span></div>
    <div class="footer">© 2013 Veltro Bonding. All Rights Reserved.</div>
    <div class="page-no">10</div>
  </section>

  <!-- Line chart slide -->
  <section class="slide c1 r3">
    <h2 class="slide-head">Graph Slide – Example 3</h2>
    <svg style="position:absolute;left:0;top:0" width="372" height="279" viewBox="0 0 372 279">
      <text x="186" y="82" font-size="6.5" font-weight="700" fill="#444" text-anchor="middle">Graph Title</text>
      <line x1="31" y1="229" x2="342" y2="229" stroke="#ccc" stroke-width=".7"/>
      <polyline points="69,162 147,176 225,113 302,147" fill="none" stroke="var(--line-grey)" stroke-width="1.4"/>
      <polyline points="69,211 147,208 225,180 302,102" fill="none" stroke="var(--blue)" stroke-width="1.4"/>
      <g fill="#fff" stroke="var(--line-grey)" stroke-width="1">
        <circle cx="69" cy="162" r="2"/><circle cx="147" cy="176" r="2"/><circle cx="225" cy="113" r="2"/><circle cx="302" cy="147" r="2"/>
      </g>
      <g fill="#fff" stroke="var(--blue)" stroke-width="1">
        <circle cx="69" cy="211" r="2"/><circle cx="147" cy="208" r="2"/><circle cx="225" cy="180" r="2"/><circle cx="302" cy="102" r="2"/>
      </g>
      <g font-size="5.5" fill="#444" text-anchor="middle">
        <text x="69" y="157">4,4</text><text x="147" y="171">3,6</text><text x="225" y="108">7,5</text><text x="302" y="142">5,3</text>
        <text x="69" y="206">1,2</text><text x="147" y="203">1,4</text><text x="225" y="175">3,2</text><text x="302" y="97">8,2</text>
        <text x="69" y="240">1st Qtr</text><text x="147" y="240">2nd Qtr</text><text x="225" y="240">3rd Qtr</text><text x="302" y="240">4th Qtr</text>
      </g>
      <rect x="95" y="100" width="70" height="33" rx="4" fill="var(--blue)"/>
      <path d="M110 133 L116 133 L108 140 Z" fill="var(--blue)"/>
      <text x="130" y="115" font-size="6" fill="#fff" text-anchor="middle">Key conclusion</text>
      <text x="130" y="123" font-size="6" fill="#fff" text-anchor="middle">added here...</text>
    </svg>
    <div class="wordmark corner-mark" style="font-size:7px;color:var(--ink)">VELTRO BONDING <span class="dot" style="width:5px;height:5px"></span></div>
    <div class="footer">© 2013 Veltro Bonding. All Rights Reserved.</div>
    <div class="page-no">12</div>
  </section>

  <!-- End slide with contact -->
  <section class="slide c2 r3">
    <div class="end-logo">
      <div class="wordmark" style="font-size:17px;color:var(--ink)">VELTRO BONDING <span class="dot" style="width:10px;height:10px"></span></div>
      <div class="url">www.veltrobonding.example</div>
    </div>
    <div class="thanks">Thank You For Your Time!</div>
    <div class="contact">
      VELTRO BONDING AB • Kvarngatan 14 • 411 02 Göteborg, Sweden<br>
      Tel +46 31 000 0100 • Fax +46 31 000 0101<br>
      www.veltrobonding.example
    </div>
    <div class="footer">© 2013 Veltro Bonding. All Rights Reserved.</div>
  </section>

  <!-- End slide alternative -->
  <section class="slide c3 r3">
    <div class="hero"><div class="wordmark on-blue" style="font-size:28px">VELTRO BONDING <span class="dot" style="width:18px;height:18px"></span></div></div>
    <div class="hero-caption" style="top:219px;font-size:13px;color:var(--ink)">Thank You!</div>
    <div class="foot-bar"></div>
    <div class="footer">© 2013 Veltro Bonding. All Rights Reserved.</div>
  </section>

</div>
</body>
</html>
```